Horse related business entrepreneur needs a business card

I need a business card design for my horse related business. The enterprise is Copper Vale LLC and I have 3 businesses (headquartered at 2 locations): 1. property management where we rent horse stalls and apartments at a thoroughbred training center outside Ocala; 2. a medium sized transportation service in central Florida that sells horse bedding and removes used horse bedding from horse farms; and horse racing

```html
<!DOCTYPE html>
<html lang="en">
<head>
<meta charset="utf-8">
<title>Copper Vale Farm – Business Card</title>
<link rel="stylesheet" href="https://fonts.googleapis.com/css2?family=Crimson+Pro:ital,wght@0,400;0,600;1,400;1,600&display=swap">
<style>
  :root {
    --teal-ink: #1f5f78;
    --copper: #e07048;
    --card: #ffffff;
    --backdrop: #e9efee;
    --black: #1b1b1b;
  }
  * { box-sizing: border-box; margin: 0; padding: 0; }
  html, body { width: 1200px; height: 1200px; overflow: hidden; }
  body {
    background: var(--backdrop);
    font-family: "Crimson Pro", Georgia, serif;
    display: flex;
    flex-direction: column;
    align-items: center;
    justify-content: center;
    gap: 60px;
  }
  .card {
    width: 840px;
    height: 480px;
    background: var(--card);
    position: relative;
    box-shadow: 0 2px 10px rgba(0,0,0,0.08);
  }

  /* Brand block */
  .brand { display: flex; flex-direction: column; align-items: center; }
  .brand__rule { height: 2px; background: var(--copper); }
  .brand__name {
    color: var(--teal-ink);
    font-weight: 600;
    text-transform: uppercase;
    letter-spacing: 0.08em;
    line-height: 1;
  }
  .brand__tagline { color: var(--copper); font-style: italic; font-weight: 600; }

  /* Front */
  .card--front { display: flex; align-items: center; justify-content: center; }
  .card--front .brand__rule { width: 420px; margin-bottom: 14px; }
  .card--front .brand__name { font-size: 56px; }
  .card--front .brand__tagline { font-size: 30px; margin-top: 8px; }

  /* Back */
  .card--back .brand { position: absolute; top: 56px; left: 0; right: 0; }
  .card--back .brand__rule { width: 250px; margin-bottom: 8px; }
  .card--back .brand__name { font-size: 36px; }
  .card--back .brand__tagline { font-size: 20px; margin-top: 4px; }

  .divider {
    position: absolute;
    left: 70px; right: 56px; top: 160px;
    height: 2px; background: var(--teal-ink);
  }

  .contact {
    position: absolute;
    left: 56px; top: 180px;
    list-style: none;
    color: var(--teal-ink);
    font-size: 21px;
    line-height: 1.35;
  }
  .contact__item { display: flex; align-items: center; gap: 12px; }
  .contact__icon { width: 16px; height: 16px; flex: none; fill: none; stroke: var(--teal-ink); stroke-width: 1.8; }
  .contact__item--indent { padding-left: 28px; }

  .signature {
    position: absolute;
    right: 96px; top: 290px;
    text-align: center;
  }
  .signature__role {
    font-size: 16px; font-weight: 600; color: var(--black);
    letter-spacing: 0.08em;
    border-bottom: 2px solid var(--black);
    padding: 0 18px 2px;
    display: inline-block;
  }
  .signature__name {
    font-size: 28px; font-weight: 600; color: var(--teal-ink);
    letter-spacing: 0.04em; text-transform: uppercase;
    margin-top: 2px;
  }
</style>
</head>
<body>

  <section class="card card--front" aria-label="Card front">
    <div class="brand">
      <div class="brand__rule"></div>
      <div class="brand__name">Copper Vale Farm</div>
      <div class="brand__tagline">Stall Rental · Fernwood FL</div>
    </div>
  </section>

  <section class="card card--back" aria-label="Card back">
    <div class="brand">
      <div class="brand__rule"></div>
      <div class="brand__name">Copper Vale Farm</div>
      <div class="brand__tagline">Stall Rental · Fernwood FL</div>
    </div>

    <div class="divider"></div>

    <ul class="contact">
      <li class="contact__item">
        <svg class="contact__icon" viewBox="0 0 16 16"><circle cx="8" cy="8" r="6.5"/><path d="M1.5 8h13M8 1.5c2.5 2 2.5 11 0 13M8 1.5c-2.5 2-2.5 11 0 13"/></svg>
        <span>dana@coppervale.com</span>
      </li>
      <li class="contact__item">
        <svg class="contact__icon" viewBox="0 0 16 16"><path d="M4 1.5l2.5 3-1.5 1.5c.8 2 2.5 3.7 4.5 4.5l1.5-1.5 3 2.5-1.5 2.5C7 14 2 9 1.5 3z"/></svg>
        <span>(555) 236-9180</span>
      </li>
      <li class="contact__item">
        <svg class="contact__icon" viewBox="0 0 16 16"><rect x="4" y="1.5" width="8" height="13" rx="1.5"/><path d="M7 12.5h2"/></svg>
        <span>(555) 472-3315</span>
      </li>
      <li class="contact__item">
        <svg class="contact__icon" viewBox="0 0 16 16"><path d="M2 8l6-5.5L14 8M4 7v7h8V7"/></svg>
        <span>2150 SE 96<sup>th</sup> Terrace Fernwood, FL 32601</span>
      </li>
      <li class="contact__item contact__item--indent">718 Alder Ridge Way Millbrook, VA 22001</li>
    </ul>

    <div class="signature">
      <div class="signature__role">OWNER</div>
      <div class="signature__name">Dana Whitlow</div>
    </div>
  </section>

</body>
</html>
```